Atelier Vane Architecture business card

We need to update our business card. We do high end custom residential, hospitality, and wellness architecture. We focus on creating unique spaces and design around the five senses, believing that architecture's true impact is not on our surroundings, but within us. We would like to see designs are instill a sense of calm awe. They should be crisp, fresh, clean, authentic, & contemporary without being sterile, overworked, or harsh. White space is important. Alternative materials are an option if natural. We have created our own logo and would like designs to incorporate it. However, we are willing to see alternatives if the logo becomes a stumbling block and you have an alternate you suggest. Card must have the following information:
Atelier Vane Architecture, Inc.
742 Marbury Rd. NE Atlanta, GA 30319
Dominic K. Whitlow, AIA, NCARB, LEED AP BD+C
ateliervane.example

Target Market(s)

Higher net worth individuals with an appreciation for design, nature, sustainability,

Industry/Entity Type

Architect

Contact Information for Business Card

See above. The title of Owner or Architect is helpful but not necessary. Minimalism should trump additional information.

Font styles to use
Serif
Sans Serif

Requirements
Must have
• It should look professional. It must use logo
Should not have
• caligraphy, animals, anything that is cute,

```html
<!DOCTYPE html>
<html lang="en">
<head>
<meta charset="utf-8">
<title>Atelier Vane Architecture – Business Card</title>
<link rel="stylesheet" href="https://fonts.googleapis.com/css2?family=EB+Garamond:ital,wght@0,400;0,600;1,400&display=swap">
<style>
  :root {
    --forest: #077619;
    --paper: #ffffff;
    --backdrop: #ececec;
    --ink: #2a2a2a;
    --on-green: #ffffff;
  }
  html, body {
    margin: 0;
    padding: 0;
    width: 1200px;
    height: 586px;
    overflow: hidden;
    background: var(--backdrop);
    font-family: "EB Garamond", Georgia, serif;
  }
  .stage {
    position: relative;
    width: 1200px;
    height: 586px;
  }
  .card {
    position: absolute;
    top: 129px;
    width: 501px;
    height: 300px;
    overflow: hidden;
  }
  .card--front {
    left: 65px;
    background: var(--forest);
  }
  .card--back {
    left: 608px;
    background: var(--paper);
  }
  .wordmark {
    margin: 0;
    font-weight: 400;
    text-transform: uppercase;
    line-height: 1.25;
  }
  .card--front .wordmark {
    position: absolute;
    left: 0;
    right: 0;
    top: 112px;
    text-align: center;
    color: var(--on-green);
    font-size: 26px;
    letter-spacing: 0.32em;
    padding-left: 0.32em;
  }
  .brush-mark {
    position: absolute;
    left: 136px;
    top: 25px;
    width: 92px;
    height: 92px;
    border-radius: 18px;
    background: var(--forest);
  }
  .card--back .wordmark {
    position: absolute;
    left: 240px;
    top: 52px;
    color: var(--ink);
    font-size: 14px;
    letter-spacing: 0.24em;
  }
  .hill {
    position: absolute;
    left: 0;
    top: 0;
    width: 501px;
    height: 300px;
  }
  .contact {
    position: absolute;
    left: 0;
    right: 0;
    top: 174px;
    text-align: center;
    color: var(--on-green);
  }
  .contact__name {
    margin: 0;
    font-size: 18px;
    font-weight: 600;
    line-height: 1.2;
  }
  .contact__credentials {
    margin: 2px 0 0;
    font-size: 10.5px;
    font-style: italic;
  }
  .contact__firm {
    margin: 22px 0 0;
    font-size: 14px;
    font-weight: 600;
  }
  .contact__address {
    margin: 2px 0 0;
    font-size: 14px;
  }
</style>
</head>
<body>
<main class="stage">
  <section class="card card--front" aria-label="Card front">
    <h1 class="wordmark">Atelier Vane<br>Architecture</h1>
  </section>

  <section class="card card--back" aria-label="Card back">
    <div class="brush-mark" role="img" aria-label="Green brush-stroke mark"></div>
    <p class="wordmark">Atelier Vane<br>Architecture</p>

    <svg class="hill" viewBox="0 0 501 300" aria-hidden="true">
      <path d="M0 271 C 60 107 441 107 501 279 V300 H0 Z" fill="var(--forest)"/>
    </svg>

    <div class="contact">
      <p class="contact__name">Dominic K. Whitlow</p>
      <p class="contact__credentials">AIA, NCARB, LEED AP BD+C</p>
      <p class="contact__firm">Atelier Vane Architecture, Inc.</p>
      <p class="contact__address">742 Marbury Rd. NE Atlanta, GA 30319</p>
    </div>
  </section>
</main>
</body>
</html>
```